One of Australia's fastest growing Financial Company looking for an updated business card design!

Meridale Holdings Australia is looking for an updated design for our business cards. We would like to keep up our professional appearances and have get new exciting design that fits our company.

The Meridale aim is to facilitate and assist clients in every financial requirement that may arise in financial areas.

We would to see the design to use colour blue and we like the clouds in the background. We have attached two designs we have use before but we need something with more professional and easy to read design.

We would like the website in the back of the card; the employees name more central and stands out; only a postal address; a list of all our locations along the bottom (Sydney, Melbourne, Brisbane, Singapore)

Looking forward to seeing the designs come in!

Target Market(s)

Other Industry Professionals
Middle Class Families

Industry/Entity Type

Finance

Contact Information for Business Card

Name; Company Role; Office Number; Mobile Number; Email Address; Website; Postal Address; Locations

Font styles to use
Serif
Sans Serif

Colors
0492cd
33a6d7
85cae6
85acd3
3176b5
0455a3
cee9f5
d5e2ee

Requirements
Must have
• Name; Company Role; Office Number; Mobile Number; Email Address; Website; Postal Address; Locations
Nice to have
• The colour blue, clouds on the background

```html
<!DOCTYPE html>
<html lang="en">
<head>
<meta charset="utf-8">
<title>Meridale Holdings Australia – Business Card</title>
<link rel="stylesheet" href="https://fonts.googleapis.com/css2?family=Source+Sans+3:wght@400;600&display=swap">
<style>
  :root {
    --brand-blue: #0c56a5;
    --sky-blue: #2aa0d8;
    --pale-blue: #cfe9f8;
    --band-blue: #d2e9f6;
    --soft-blue: #5aaad9;
    --mid-blue: #1a6fb8;
    --accent-red: #e8262f;
    --text-grey: #555a60;
    --page-bg: #ececec;
    --card-white: #ffffff;
  }
  * { box-sizing: border-box; margin: 0; padding: 0; }
  html, body {
    width: 1200px; height: 1200px; overflow: hidden;
    background: var(--page-bg);
    font-family: "Source Sans 3", "Myriad Pro", sans-serif;
  }
  .card {
    position: absolute; left: 175px; width: 851px; height: 481px;
    border-radius: 24px; overflow: hidden;
  }
  .card--front { top: 90px; background: var(--brand-blue); }
  .card--back { top: 630px; background: var(--card-white); }

  .front__name {
    position: absolute; left: 133px; top: 190px;
    font-size: 92px; font-weight: 600; letter-spacing: -1px;
    color: var(--pale-blue); line-height: 1;
  }
  .front__accent {
    position: absolute; left: 578px; top: 110px;
    width: 272px; height: 272px; border-radius: 50%;
    background: var(--mid-blue);
  }

  .back__accent {
    position: absolute; left: 25px; top: 114px;
    width: 256px; height: 256px; border-radius: 50%;
    background: var(--soft-blue); opacity: .8;
  }
  .person { position: absolute; left: 345px; top: 128px; }
  .person__name {
    font-size: 39px; font-weight: 400; color: var(--brand-blue); line-height: 1;
  }
  .person__role {
    margin-top: 6px; font-size: 24px; color: var(--sky-blue); line-height: 1;
  }
  .contact-band {
    position: absolute; left: 300px; right: 0; top: 232px; height: 164px;
    background: linear-gradient(90deg, rgba(210,233,246,0) 0%, var(--band-blue) 100%);
  }
  .contact-list {
    position: absolute; left: 345px; top: 252px; list-style: none;
  }
  .contact-list li {
    display: flex; align-items: center; height: 33px;
    font-size: 24px; color: var(--text-grey);
  }
  .contact-list svg { width: 20px; height: 20px; margin-right: 15px; flex: none; }
  .locations {
    position: absolute; left: 0; right: 0; bottom: 0; height: 59px;
    background: var(--brand-blue);
    display: flex; align-items: center; justify-content: center; gap: 18px;
    color: var(--card-white); font-size: 26px; letter-spacing: 5px;
  }
  .locations__sep { width: 2px; height: 26px; background: var(--accent-red); }
</style>
</head>
<body>

<section class="card card--front">
  <div class="front__accent"></div>
  <div class="front__name">Meridale</div>
</section>

<section class="card card--back">
  <div class="back__accent"></div>
  <div class="person">
    <h1 class="person__name">Clara Hensley</h1>
    <p class="person__role">Investment Consultant</p>
  </div>
  <div class="contact-band"></div>
  <ul class="contact-list">
    <li>
      <svg viewBox="0 0 20 20" fill="var(--accent-red)"><path d="M1 7c0-3 4-4 9-4s9 1 9 4v2h-4V7c-1-1-9-1-10 0v2H1z"/><rect x="3" y="10" width="14" height="8" rx="2"/><circle cx="10" cy="14" r="2.3" fill="#fff"/></svg>
      (00) 000.000.0000
    </li>
    <li>
      <svg viewBox="0 0 20 20" fill="none" stroke="var(--accent-red)" stroke-width="2.4"><rect x="5" y="1.5" width="10" height="17" rx="1.5"/><circle cx="10" cy="15" r=".6" fill="var(--accent-red)"/></svg>
      (00) 000.000.0000
    </li>
    <li>
      <svg viewBox="0 0 20 20"><rect x="1" y="4" width="18" height="13" fill="var(--accent-red)"/><path d="M2 5l8 7 8-7M2 16l6-5M18 16l-6-5" stroke="#fff" stroke-width="1.5" fill="none"/></svg>
      cla@meridaleholdinggroup.com.au
    </li>
    <li>
      <svg viewBox="0 0 20 20"><circle cx="10" cy="10" r="9" fill="var(--accent-red)"/><g stroke="#fff" stroke-width="1.2" fill="none"><ellipse cx="10" cy="10" rx="4" ry="9"/><path d="M1 10h18M2.5 5.5h15M2.5 14.5h15M10 1v18"/></g></svg>
      www.meridaleholdinggroup.com.au
    </li>
  </ul>
  <footer class="locations">
    <span>Sydney</span><span class="locations__sep"></span>
    <span>Melbourne</span><span class="locations__sep"></span>
    <span>Brisbane</span><span class="locations__sep"></span>
    <span>Singapore</span>
  </footer>
</section>

</body>
</html>
```